Business Card Design Project

I would like to redesign our business cards and change the look and feel of our marketing material, but maintain the same basic identity of our current logo.
It is my belief that it could be much better.
You can view our website at kbozt.com

   

I was looking for a completely different look.  Something much more hip and cool looking.  You can change the colors.

I like this look and feel

 http://www.omdlawfirm.com

 But obviously don’t want to copy them exactly.

 

For the back just leave the last point.

“Focus on Your Business, and We’ll Focus on Your Claim”

I want there to be space for someone to write on.

                                                                    

                                       

I like this look and feel

 http://www.omdlawfirm.com

```html
<!DOCTYPE html>
<html lang="en">
<head>
<meta charset="utf-8">
<title>Halden Claim Advisors – Business Card</title>
<link rel="stylesheet" href="https://fonts.googleapis.com/css2?family=EB+Garamond:wght@400;500&display=swap">
<style>
  :root {
    --page-bg: #e4e6ee;
    --card-bg: #ffffff;
    --orange: #e8901f;
    --amber: #e9ac25;
    --gold: #f0c34a;
    --blue-deep: #1f6fba;
    --blue-mid: #2b8ed1;
    --blue-light: #4f9fd9;
    --ink: #2a2a2a;
    --ink-light: #ffffff;
  }
  * { margin: 0; padding: 0; box-sizing: border-box; }
  html, body {
    width: 1200px; height: 796px; overflow: hidden;
    background: var(--page-bg);
    font-family: "EB Garamond", Garamond, serif;
    color: var(--ink);
  }
  .canvas {
    position: relative; width: 1200px; height: 796px;
    display: flex; justify-content: center; align-items: center; gap: 60px;
  }
  .card {
    position: relative; width: 520px; height: 290px;
    background: var(--card-bg);
    box-shadow: 0 2px 10px rgba(0,0,0,0.12);
    overflow: hidden;
  }
  .band { position: absolute; }

  /* Front */
  .band--company { left: 0; top: 66px; width: 262px; height: 23px; background: var(--orange); }
  .band--name { left: 262px; top: 84px; width: 258px; height: 27px; background: var(--orange); }
  .company-name {
    position: absolute; left: 6px; top: 67px;
    font-size: 14px; letter-spacing: 0.2px; color: var(--ink-light);
    white-space: nowrap;
  }
  .person-name {
    position: absolute; left: 262px; width: 258px; top: 86px;
    text-align: center; font-size: 18px; color: var(--ink);
  }
  .contact {
    position: absolute; left: 272px; top: 133px;
    list-style: none; font-size: 15px; line-height: 21px;
  }
  .band--foot-a { left: 0; top: 241px; width: 180px; height: 26px; background: var(--orange); }
  .band--foot-b { left: 180px; top: 241px; width: 175px; height: 26px; background: var(--amber); }
  .band--foot-c { left: 355px; top: 241px; width: 165px; height: 26px; background: var(--gold); }
  .address-street, .address-city {
    position: absolute; top: 244px; font-size: 14px; color: var(--ink);
    white-space: nowrap;
  }
  .address-street { left: 12px; }
  .address-city { right: 14px; }

  /* Back */
  .band--top-left { left: 0; top: 76px; width: 262px; height: 22px; background: var(--blue-deep); }
  .band--top-right { left: 262px; top: 86px; width: 258px; height: 24px; background: var(--blue-deep); }
  .tagline {
    position: absolute; left: 0; width: 100%; top: 164px;
    text-align: center; font-size: 16px; color: var(--ink);
    white-space: nowrap;
  }
  .band--base-a { left: 0; top: 248px; width: 175px; height: 26px; background: var(--blue-deep); }
  .band--base-b { left: 175px; top: 248px; width: 175px; height: 26px; background: var(--blue-mid); }
  .band--base-c { left: 350px; top: 248px; width: 170px; height: 26px; background: var(--blue-light); }
</style>
</head>
<body>
<main class="canvas">
  <section class="card card--front" aria-label="Card front">
    <div class="band band--company"></div>
    <div class="band band--name"></div>
    <p class="company-name">HALDEN CLAIM ADVISORS</p>
    <p class="person-name">Daniel Avery</p>
    <ul class="contact">
      <li>office : 516-555-0142</li>
      <li>cell : 917-555-0187</li>
      <li>www.kbozt.com</li>
      <li>da@kbozt.com</li>
    </ul>
    <div class="band band--foot-a"></div>
    <div class="band band--foot-b"></div>
    <div class="band band--foot-c"></div>
    <p class="address-street">210 Harbor Lane</p>
    <p class="address-city">Millbrook , Ny 11590</p>
  </section>

  <section class="card card--back" aria-label="Card back">
    <div class="band band--top-left"></div>
    <div class="band band--top-right"></div>
    <p class="tagline">“Mind Your Work, and Let Us Mind Every Recovery”</p>
    <div class="band band--base-a"></div>
    <div class="band band--base-b"></div>
    <div class="band band--base-c"></div>
  </section>
</main>
</body>
</html>
```